Marlow Law Stationery - Letterhead, Envelopes, Business Cards

We need high quality business stationery for our Personal Injury Law Firm located in Houston, Texas. The design should include the logo, Marlow Law Group, PLLC, 713-555-4718, 2150 Fernbrook Avenue, Suite 310, Houston, Texas 77019 www.MarlowLaw.example. The colors are blue and white. The letterhead should also include the Attorneys - Tessa Quill, Mitchell R. Marlow and Derek Hale.

```html
<!DOCTYPE html>
<html lang="en">
<head>
<meta charset="utf-8">
<title>Marlow Law – Business Card</title>
<link rel="stylesheet" href="https://fonts.googleapis.com/css2?family=Montserrat:wght@400;500;700;800&display=swap">
<style>
  :root {
    --stage: #0c0c0d;
    --navy: #0d1b3e;
    --navy-deep: #0a1a40;
    --navy-raised: #173061;
    --ink: #1c2340;
    --paper: #ffffff;
  }
  * { box-sizing: border-box; margin: 0; padding: 0; }
  html, body { width: 1200px; height: 800px; overflow: hidden; }
  body {
    background: var(--stage);
    font-family: "Montserrat", sans-serif;
    display: flex;
    align-items: center;
    justify-content: center;
    gap: 70px;
  }
  .card {
    width: 440px;
    height: 480px;
    border-radius: 34px;
    display: flex;
    flex-direction: column;
    align-items: center;
  }
  .card--back {
    background: var(--navy-deep);
    justify-content: center;
  }
  .back-mark {
    font-weight: 800;
    font-size: 56px;
    color: var(--navy-raised);
    letter-spacing: 1px;
  }
  .card--front {
    background: var(--paper);
    color: var(--ink);
    padding-top: 70px;
    text-align: center;
  }
  .front-mark {
    display: flex;
    align-items: center;
    gap: 12px;
    font-weight: 800;
    font-size: 30px;
    color: var(--navy);
    margin-bottom: 36px;
  }
  .front-mark__dot {
    width: 26px; height: 26px;
    border-radius: 50%;
    background: var(--navy);
  }
  .holder-name {
    font-weight: 800;
    font-size: 26px;
    color: var(--navy);
    letter-spacing: 0.5px;
    text-transform: uppercase;
  }
  .holder-role {
    font-weight: 400;
    font-size: 15px;
    margin-top: 6px;
    letter-spacing: 0.5px;
  }
  .contact-icons {
    display: flex;
    gap: 8px;
    margin: 22px 0 14px;
  }
  .contact-icons svg { width: 22px; height: 22px; }
  .contact-line {
    font-size: 15px;
    font-weight: 500;
    line-height: 1.6;
  }
  .divider {
    width: 130px;
    height: 2px;
    background: var(--navy);
    margin: 18px 0;
  }
  .address {
    font-size: 15px;
    font-weight: 500;
    line-height: 1.6;
  }
</style>
</head>
<body>
  <section class="card card--back" aria-label="Business card back">
    <span class="back-mark">Marlow Law</span>
  </section>

  <section class="card card--front" aria-label="Business card front">
    <div class="front-mark">
      <span class="front-mark__dot"></span>
      <span>Marlow Law</span>
    </div>
    <h1 class="holder-name">Mitchell R. Marlow</h1>
    <p class="holder-role">Attorneys</p>
    <div class="contact-icons">
      <svg viewBox="0 0 24 24" aria-label="Phone">
        <circle cx="12" cy="12" r="12" fill="#0d1b3e"/>
        <path d="M8.5 6.5l2 2.2-1.2 1.5a8 8 0 0 0 4.5 4.5l1.5-1.2 2.2 2-1.3 2a10 10 0 0 1-9.7-9.7z" fill="#fff"/>
      </svg>
      <svg viewBox="0 0 24 24" aria-label="Website">
        <circle cx="12" cy="12" r="12" fill="#0d1b3e"/>
        <circle cx="12" cy="12" r="6.5" fill="none" stroke="#fff" stroke-width="1.4"/>
        <ellipse cx="12" cy="12" rx="2.8" ry="6.5" fill="none" stroke="#fff" stroke-width="1.2"/>
        <line x1="5.5" y1="12" x2="18.5" y2="12" stroke="#fff" stroke-width="1.2"/>
      </svg>
    </div>
    <p class="contact-line">713-555-4718<br>www.MarlowLaw.example</p>
    <div class="divider"></div>
    <p class="address">2150 Fernbrook Avenue,<br>Suite 310, Houston, Texas 77019</p>
  </section>
</body>
</html>
```